Wine Bottle Lable

Want a unique, simple but elegant, label for a wine bottle. I want to use the letters "TWG" in the design which is a moniker for my last name "Tallwidge". The letters TWG do not have to be juxtaposed together so that it is recognizable, or they could be something like T-WG, WG-T, TGW T-WG-T, etc. The X could be totally separated from the NO, or otherwise. The wine is a white wine in a clear bottle. I need Adobe Illustrator files so I can add the wine varietal, year, alcohol content. The label should be 4" wide and 5" tall.

Colors

Designer to choose colors to be used in the design.

Requirements
Nice to have
• outstanding but simple graphics

```html
<!DOCTYPE html>
<html lang="en">
<head>
<meta charset="utf-8">
<title>Tallwidge Wine Label</title>
<link rel="stylesheet" href="https://fonts.googleapis.com/css2?family=Playfair+Display:wght@400&family=Oswald:wght@600&family=Jost:wght@300;400&display=swap">
<style>
  :root {
    --backdrop: #ececec;
    --label-paper: #ffffff;
    --gold: #bba65c;
    --ink-grey: #7b7b7b;
    --ink-dark: #3a3a3a;
  }
  html, body {
    margin: 0;
    width: 1200px;
    height: 1000px;
    overflow: hidden;
    background: var(--backdrop);
  }
  .canvas {
    position: relative;
    width: 1200px;
    height: 1000px;
  }
  .wine-label {
    position: absolute;
    left: 280px;
    top: 100px;
    width: 640px;
    height: 800px;
    background: var(--label-paper);
    box-shadow: 0 2px 10px rgba(0, 0, 0, 0.12);
    overflow: hidden;
  }
  .wine-label svg {
    display: block;
    width: 640px;
    height: 800px;
  }
  .monogram-initial {
    fill: var(--gold);
  }
  .monogram-pair {
    font-family: "Playfair Display", serif;
    font-size: 78px;
    fill: var(--gold);
  }
  .monogram-rule {
    stroke: var(--gold);
    stroke-width: 2;
  }
  .vintage {
    font-family: "Jost", sans-serif;
    font-weight: 300;
    font-size: 38px;
    fill: var(--ink-dark);
  }
  .varietal {
    font-family: "Oswald", sans-serif;
    font-weight: 600;
    font-size: 38px;
    letter-spacing: 0.5px;
    fill: var(--gold);
  }
  .volume {
    font-family: "Jost", sans-serif;
    font-weight: 400;
    font-size: 30px;
    fill: var(--ink-grey);
  }
  .volume-unit {
    font-size: 22px;
  }
</style>
</head>
<body>
  <main class="canvas">
    <section class="wine-label" aria-label="Tallwidge wine label">
      <svg viewBox="0 0 640 800" xmlns="http://www.w3.org/2000/svg">
        <path class="monogram-initial"
              d="M22 30 H380 V118 H373 Q368 52 310 45 H212 V738 Q214 758 262 762 V772 H98 V762 Q146 758 148 738 V45 H90 Q34 52 29 118 H22 Z"/>

        <text class="monogram-pair" x="289" y="256">WG</text>
        <line class="monogram-rule" x1="289" y1="267" x2="414" y2="267"/>

        <text class="vintage" x="440" y="590">2019</text>
        <text class="varietal" x="440" y="631">WINE</text>
        <text class="varietal" x="440" y="667">VARIETAL</text>

        <text class="volume" x="440" y="776">750<tspan class="volume-unit" dx="6">ML</tspan></text>
      </svg>
    </section>
  </main>
</body>
</html>
```